Natural Light/Organic/Documentary Photography Business

I like a simple, approachable, feminine, earthy/organic feel. Earth/neutral tones, nothing too loud or obnoxious. I like the watercolor look. I don't want anything too trendy or something I'll get tired of after a couple months. As far as colors, I am much more a fan of cream/taupe/blue/green...not a fan of pink or purple at all.

Target Market(s)

Weddings & Families

Industry/Entity Type

Wedding Photography

Contact Information for Business Card

website, email, phone number

Font styles to use
Other font styles liked:
• Horizontes, Gotham

Colors

Designer to choose colors to be used in the design.

Requirements
Must have
• Website: www.elspethmarlowe.com
• Phone: 412.638.9057
• Email: elspeth@elspethmarlowe.com
Nice to have
• I like the watercolor look but its not necessary. I like simple/earthy tones. Nothing too loud or distracting. Simple & feminine without being too girly. I like an approachable/soft feel.
• Instagram: www.instagram.com/elspethmarlowephotography/
Should not have
• NO loud colors or design or pattern. I do not want a photo of a camera or lens or anything cheesy like that.

```html
<!DOCTYPE html>
<html lang="en">
<head>
<meta charset="utf-8">
<title>Elspeth Marlowe Photography — Business Card</title>
<link rel="stylesheet" href="https://fonts.googleapis.com/css2?family=Montserrat:wght@300;400&display=swap">
<style>
  :root {
    --backdrop: #262626;
    --card-taupe: #bdb6ad;
    --card-white: #fbfbfa;
    --mark-on-taupe: #d6d1ca;
    --ink-taupe: #8f877e;
    --rule-taupe: #a39b92;
  }
  * { box-sizing: border-box; margin: 0; padding: 0; }
  html, body {
    width: 1200px;
    height: 1200px;
    overflow: hidden;
    background: var(--backdrop);
    font-family: "Montserrat", sans-serif;
  }
  .sheet {
    width: 1200px;
    height: 1200px;
    display: flex;
    flex-direction: column;
    align-items: center;
    justify-content: center;
    gap: 80px;
  }
  .card {
    width: 840px;
    height: 480px;
    position: relative;
  }
  .card--front {
    background: var(--card-taupe);
    display: flex;
    align-items: center;
    justify-content: center;
  }
  .card--back {
    background: var(--card-white);
    display: flex;
    align-items: center;
    justify-content: space-between;
    padding: 0 70px;
  }
  .brand {
    display: flex;
    flex-direction: column;
    align-items: flex-end;
    font-weight: 300;
  }
  .brand__name {
    font-size: 46px;
    letter-spacing: 1px;
    line-height: 1;
  }
  .brand__tag {
    font-size: 11px;
    letter-spacing: 6px;
    margin-top: 8px;
  }
  .card--front .brand { color: var(--mark-on-taupe); }
  .card--back .brand { color: var(--ink-taupe); }
  .card--back .brand__name { font-size: 30px; }
  .card--back .brand__tag { font-size: 8px; letter-spacing: 4.5px; margin-top: 6px; }
  .contact {
    display: flex;
    align-items: center;
    gap: 26px;
    color: var(--ink-taupe);
  }
  .contact__rule {
    width: 1px;
    height: 120px;
    background: var(--rule-taupe);
  }
  .contact__list {
    list-style: none;
    font-size: 19px;
    font-weight: 300;
    line-height: 1.45;
  }
</style>
</head>
<body>
  <main class="sheet">
    <section class="card card--front" aria-label="Card front">
      <div class="brand">
        <span class="brand__name">Elspeth Marlowe</span>
        <span class="brand__tag">PHOTOGRAPHY</span>
      </div>
    </section>

    <section class="card card--back" aria-label="Card back">
      <div class="brand">
        <span class="brand__name">Elspeth Marlowe</span>
        <span class="brand__tag">PHOTOGRAPHY</span>
      </div>
      <div class="contact">
        <span class="contact__rule"></span>
        <ul class="contact__list">
          <li>412.638.9057</li>
          <li>elspeth@elspethmarlowe.com</li>
          <li>www.elspethmarlowe.com</li>
        </ul>
      </div>
    </section>
  </main>
</body>
</html>
```